LET ME HANDLE YOUR AUCTION NEEDS!

I am here to handle all your auction needs, I have over 20 years of auction experience buying and selling for dealerships in North Carolina and Tennessee. Send me to the sale to either rep your vehicles or let me know what you need and I can be
another set of eyes to help you buy what is hot and bad credit cars are my specialty. You know a car always sells better with a familiar face rather than auction personnel and with my great reputation I will be able to help find the buyers for your aged inventory.
Call me today and let's get started.
Rick Halvorsen 555-862-3917
(please have pictures of vehicles or an auto auction in the design)

```html
<!DOCTYPE html>
<html lang="en">
<head>
<meta charset="utf-8">
<title>Auction Needs – Rick Halvorsen</title>
<link href="https://fonts.googleapis.com/css2?family=Alfa+Slab+One&family=Kaushan+Script&family=Roboto+Condensed:wght@700;900&family=Open+Sans:wght@800&display=swap" rel="stylesheet">
<style>
  :root {
    --orange: #f0561d;
    --orange-deep: #d9470f;
    --ink: #141414;
    --paper-top: #ffffff;
    --paper-bottom: #e4e4e4;
    --yellow: #ffe61a;
    --yellow-deep: #f4c400;
    --blue: #1f3fa8;
    --call-box: #e07a1f;
    --white: #ffffff;
  }
  * { margin: 0; padding: 0; box-sizing: border-box; }
  html, body { width: 1200px; height: 563px; overflow: hidden; background: #ffffff; }
  .flyer {
    position: relative;
    width: 1200px; height: 563px;
    overflow: hidden;
    background: radial-gradient(ellipse at 50% 35%, var(--paper-top) 40%, var(--paper-bottom) 100%);
  }
  .headline-lead {
    position: absolute; left: 78px; top: 70px;
    font-family: "Alfa Slab One", serif;
    font-size: 34px; color: var(--ink); letter-spacing: 1px;
  }
  .headline-main {
    position: absolute; left: 64px; top: 100px;
    font-family: "Alfa Slab One", serif;
    font-size: 98px; line-height: 1; letter-spacing: 4px;
    color: var(--orange);
    text-shadow: 3px 3px 0 #9b2e06, 5px 6px 8px rgba(0,0,0,.35);
  }
  .gavel-art {
    position: absolute; left: 960px; top: 14px; width: 150px; height: 84px;
    border-radius: 10px;
    background: linear-gradient(135deg, #7a1d14, #c0392b 55%, #8c8c8c);
  }
  .vehicle-lineup {
    position: absolute; left: 60px; top: 222px; width: 1080px; height: 120px;
    border-radius: 40px;
    background: linear-gradient(90deg, #6b6b6b, #c62828 18%, #1e3f9c 34%, #f4f4f4 50%, #b71c1c 66%, #6d4c41 82%, #222 100%);
    opacity: .9;
  }
  .cta-swoosh { position: absolute; left: 70px; top: 352px; }
  .cta-start {
    position: absolute; left: 100px; top: 360px;
    padding: 8px 26px;
    background: linear-gradient(180deg, var(--yellow), var(--yellow-deep));
    border-radius: 6px;
    transform: rotate(-7deg);
    font-family: "Kaushan Script", cursive;
    font-size: 40px; color: var(--ink);
    box-shadow: 2px 3px 6px rgba(0,0,0,.3);
  }
  .cta-call {
    position: absolute; left: 190px; top: 416px;
    padding: 2px 22px 6px;
    background: var(--call-box);
    font-family: "Open Sans", sans-serif;
    font-weight: 800; font-size: 44px; color: var(--white);
    letter-spacing: -1px;
    z-index: 2;
  }
  .experience-badge { position: absolute; left: 760px; top: 300px; z-index: 2; }
  .contact-band {
    position: absolute; left: 0; top: 450px; width: 1200px; height: 113px;
    background: var(--ink);
    border-top: 5px solid var(--orange);
  }
  .contact-name {
    position: absolute; left: 60px; top: 482px;
    font-family: "Alfa Slab One", serif;
    font-size: 46px; letter-spacing: 3px; color: var(--orange);
    z-index: 2;
  }
  .contact-phone {
    position: absolute; left: 600px; top: 476px;
    display: flex; align-items: center; gap: 18px;
    font-family: "Roboto Condensed", sans-serif;
    font-weight: 900; font-size: 56px; color: var(--white);
    z-index: 2;
  }
  .phone-icon { width: 58px; height: 58px; }
</style>
</head>
<body>
<main class="flyer">
  <p class="headline-lead">Let Me Handle All Of Your</p>
  <h1 class="headline-main">AUCTION NEEDS</h1>

  <div class="gavel-art" role="img" aria-label="Wooden auction gavel on its sound block"></div>

  <div class="vehicle-lineup" role="img" aria-label="Row of cars for auction: grey sedan, red coupe, blue SUV, white sedan, red jeep, brown sedan and black crossover"></div>

  <svg class="cta-swoosh" width="360" height="120" viewBox="0 0 360 120" aria-hidden="true">
    <ellipse cx="180" cy="62" rx="172" ry="50" fill="none" stroke="var(--blue)" stroke-width="4"/>
  </svg>
  <p class="cta-start">Let's Get Started</p>
  <p class="cta-call">Call now</p>

  <svg class="experience-badge" width="380" height="170" viewBox="0 0 380 170">
    <path d="M90 10 Q190 -6 290 10 L300 96 Q190 116 80 96 Z" fill="var(--orange)" stroke="var(--white)" stroke-width="3"/>
    <path d="M98 20 Q190 6 282 20 L290 88 Q190 106 90 88 Z" fill="none" stroke="var(--white)" stroke-width="2"/>
    <g fill="var(--white)">
      <polygon points="170,30 173,37 180,37 174,41 176,48 170,44 164,48 166,41 160,37 167,37"/>
      <polygon points="190,24 194,33 203,33 196,38 199,47 190,42 181,47 184,38 177,33 186,33"/>
      <polygon points="210,30 213,37 220,37 214,41 216,48 210,44 204,48 206,41 200,37 207,37"/>
    </g>
    <text x="190" y="72" text-anchor="middle" font-family="Roboto Condensed, sans-serif" font-weight="900" font-size="26" fill="var(--ink)">OVER 20 YEARS</text>
    <text x="190" y="94" text-anchor="middle" font-family="Roboto Condensed, sans-serif" font-weight="900" font-size="18" fill="var(--white)">AUCTION EXPERIENCE</text>
    <path d="M10 100 L40 104 L30 120 L42 138 L12 134 Z" fill="#333"/>
    <path d="M370 100 L340 104 L350 120 L338 138 L368 134 Z" fill="#333"/>
    <path d="M36 102 Q190 128 344 102 L344 140 Q190 166 36 140 Z" fill="#262626" stroke="var(--white)" stroke-width="1.5" stroke-dasharray="4 3"/>
    <text x="190" y="126" text-anchor="middle" font-family="Roboto Condensed, sans-serif" font-weight="700" font-size="12" fill="var(--white)" letter-spacing="1">IN BUYING AND SELLING FOR DEALERSHIPS</text>
    <text x="190" y="142" text-anchor="middle" font-family="Roboto Condensed, sans-serif" font-weight="700" font-size="12" fill="var(--white)" letter-spacing="1">IN NORTH CAROLINA AND TENNESSEE</text>
  </svg>

  <div class="contact-band"></div>
  <p class="contact-name">RICK HALVORSEN</p>
  <p class="contact-phone">
    <svg class="phone-icon" viewBox="0 0 58 58" aria-hidden="true">
      <circle cx="29" cy="29" r="26" fill="none" stroke="var(--white)" stroke-width="3"/>
      <path d="M22 16 q-6 3 -4 12 q3 11 12 15 q5 2 8 -2 l-5 -6 q-2 1 -4 0 q-4 -3 -5 -8 q0 -2 2 -3 Z" fill="var(--white)"/>
    </svg>
    555-862-3917
  </p>
</main>
</body>
</html>
```